WAGLH - 2020 Vision Banner

3 x 6-foot banner
For a Christian Church, a Theme designed Banner for 2020

Target Market(s)

Christian Congregation, internal church banner

Industry/Entity Type

Church

Font styles to use
Decorative

Colors
886aae
ffffff

Requirements
Must have
• Word-Anchored Gathering Church of Larkmoor Heights
• 2020 Vision
• Use Logo
• Color Combinations are: white, black, purple, sliver
• Communicate faith, future, and hope
Nice to have
• Bible
• Cross
Should not have
• No clip art

```html
<!DOCTYPE html>
<html lang="en">
<head>
<meta charset="utf-8">
<title>WAGLH – 2020 Vision Banner</title>
<link rel="stylesheet" href="https://fonts.googleapis.com/css2?family=Archivo+Black&family=Roboto+Condensed:wght@700&family=Roboto:wght@400&display=swap">
<style>
  :root {
    --stage: #c9c9c9;
    --purple: #663399;
    --purple-light: #886aae;
    --white: #ffffff;
    --silver-hi: #f6f6f6;
    --silver-mid: #c4c4c4;
    --silver-lo: #8a8a8a;
  }
  * { margin: 0; padding: 0; box-sizing: border-box; }
  html, body {
    width: 1200px; height: 917px; overflow: hidden;
    background: var(--stage);
  }
  .banner {
    position: absolute; left: 109px; top: 213px;
    width: 982px; height: 491px;
    background: var(--purple);
    overflow: hidden;
  }
  .banner__art { position: absolute; inset: 0; }
  .brand {
    position: absolute; left: 25px; top: 9px;
    display: flex; align-items: center; gap: 20px;
  }
  .brand__mark {
    width: 110px; height: 110px; border-radius: 50%;
    background: var(--white);
    flex: none;
  }
  .brand__name {
    font-family: "Roboto Condensed", sans-serif; font-weight: 700;
    font-size: 20px; line-height: 23px; color: var(--white);
    text-transform: uppercase; white-space: nowrap;
  }
  .brand__line { display: block; }
  .headline {
    position: absolute; left: 26px; top: 137px;
    font-family: "Archivo Black", sans-serif;
    font-size: 128px; line-height: 121px;
    text-transform: uppercase;
  }
  .headline__line {
    display: block; width: max-content;
    transform: scaleX(.75); transform-origin: left center;
    background: linear-gradient(180deg, var(--silver-hi) 0%, var(--silver-mid) 45%, var(--silver-lo) 55%, var(--silver-hi) 100%);
    -webkit-background-clip: text; background-clip: text;
    color: transparent;
  }
  .tagline {
    position: absolute; left: 30px; top: 384px;
    font-family: "Roboto Condensed", sans-serif; font-weight: 700;
    font-size: 40px; line-height: 48px; color: var(--white);
    text-transform: uppercase;
  }
  .website {
    position: absolute; left: 30px; top: 440px;
    font-family: "Roboto", sans-serif; font-size: 21px;
    color: var(--white);
  }
</style>
</head>
<body>
  <section class="banner">
    <svg class="banner__art" width="982" height="491" viewBox="0 0 982 491">
      <defs>
        <linearGradient id="silverRing" x1="0" y1="0" x2="1" y2="1">
          <stop offset="0" stop-color="#e8e8e8"/>
          <stop offset=".5" stop-color="#9a9a9a"/>
          <stop offset="1" stop-color="#dcdcdc"/>
        </linearGradient>
        <linearGradient id="photoTone" x1="0" y1="0" x2="1" y2="0">
          <stop offset="0" stop-color="#4e4e4e"/>
          <stop offset=".4" stop-color="#a0a0a0"/>
          <stop offset="1" stop-color="#f0f0f0"/>
        </linearGradient>
      </defs>
      <ellipse class="ring ring--silver" cx="772" cy="226" rx="382" ry="270" fill="url(#silverRing)"/>
      <ellipse class="ring ring--purple" cx="778" cy="228" rx="370" ry="263" fill="var(--purple-light)"/>
      <ellipse class="photo" cx="790" cy="226" rx="360" ry="254" fill="url(#photoTone)"
        role="img" aria-label="Black-and-white photo of hands raising a Holy Bible beside a stone cross against a pale sky"/>
    </svg>

    <div class="brand">
      <div class="brand__mark" aria-hidden="true"></div>
      <p class="brand__name"><span class="brand__line">Word-Anchored Gathering</span><span class="brand__line">Church of Larkmoor Heights</span></p>
    </div>

    <h1 class="headline"><span class="headline__line">2020</span><span class="headline__line">Vision</span></h1>
    <p class="tagline">Faith, Future and Hope</p>
    <p class="website">www.waglh.org</p>
  </section>
</body>
</html>
```